Flyer Needed to Advertise New Online Reading Programs

ABOUT THE TRUST OF READING DEVELOPMENT
The Trust teaches summer reading skills programs for elementary school students, in programs offered through partnerships with universities, colleges and municipalities nationwide. The goal of each program is to build reading skills, and to foster a lifetime love of books and reading.

AIMS & TARGET MARKET
The Trust has developed a new format of its’ online reading program for elementary students, which includes live small-group video classes taught by a professional reading teacher. The Trust seeks a new graphic design for a flyer to advertise the new online reading program. The flyer will be sent to elementary schools, passed out by teachers, and then taken home by students to show parents; therefore, the primary audience for the flyer will be teachers and parents of elementary school students.

Live classes for children are completely new in online education, unlike anything else in the marketplace, and parents and teachers therefore have no experience with them. The successful design will include illustrations or photographs that allow visitors to immediately grasp/understand the new video class format, without relying heavily on a written description. Additionally, the successful flyer concept will make the program, and the video classes in particular, feel fun and appealing to kids and parents.

Below is additional information about the new live small-group video class format, which meets weekly for 6 weeks:
o During video classes, students participate from home.
o During discussions, the student’s computer (or tablet) screen is filled with live video frames of the teacher and the other students. The video frame for the teacher is larger, and the other students appear in smaller frames.
o During other video class instruction, the teacher uses a presentation screen to display pages of a book or a “whiteboard” used for instructional activities.

Notes: The flyer design could include an illustrated or photo screenshot of a video class, with children looking engaged and a teacher leading them in discussion (stock photos are okay to use in flyer design). We have included a screen shot of one of these classes for reference, but do not feel constrained to represent this screen realistically (as shown here). Layout, look and feel can be changed. Alternatively, you may choose to use a graphic other than a screenshot to bring across the concept of the video classes.

COPY AND SPECIFICATIONS
The flyer design will be one-sided and the dimensions are 8.5” x 11” in either portrait or landscape orientation. We will consider designs in color or black and white. Since we brand our flyers with logos of the universities we partner with throughout the nation, we’ll need to include a partner logo in the design. Exact copy will be provided, but layout is flexible. Screenshots from our sample classes are included to show screen layout. Stock photos are okay to use in flyer designs.

Reason: We'd like to make edits to existing designs.

Hi designers, We wanted to share our thoughts on the main image of the flyer. We're leaning towards an image that shows a sole student on a computer with the computer screen in view. The computer screen could have the sample image we provided to show how the video classes operate. Thanks! The Trust of Reading Development

Graphic Design

```html
<!DOCTYPE html>
<html lang="en">
<head>
<meta charset="utf-8">
<title>Reading Skills Classes – Online this Summer</title>
<link rel="stylesheet" href="https://fonts.googleapis.com/css2?family=Open+Sans:wght@300;400;600;700&family=Roboto+Condensed:wght@400&display=swap">
<style>
  :root {
    --page-bg: #c9c9c9;
    --paper: #ffffff;
    --brand-blue: #1b8fd3;
    --heading-blue: #1a8cd3;
    --band-dark: #231f20;
    --ink: #2b2b2b;
    --hero-text: #3a3a3a;
    --hero-bg: #ecdfcf;
    --photo-light: #f1e6d8;
    --photo-mid: #d9c4ab;
    --photo-deep: #bfa68a;
    --photo-accent: #e6c9c6;
  }
  * { box-sizing: border-box; margin: 0; padding: 0; }
  html, body { width: 1200px; height: 1200px; overflow: hidden; }
  body {
    background: var(--page-bg);
    font-family: "Open Sans", Arial, sans-serif;
    position: relative;
  }
  .flyer {
    position: absolute;
    left: 180px; top: 65px;
    width: 840px; height: 1070px;
    background: var(--paper);
    overflow: hidden;
  }

  /* Hero */
  .hero { position: absolute; left: 0; top: 0; width: 840px; height: 389px; background: var(--hero-bg); }
  .hero-photo {
    position: absolute; left: 360px; top: 0;
    width: 480px; height: 389px;
    background: linear-gradient(105deg, var(--hero-bg) 0%, var(--photo-light) 18%, var(--photo-mid) 48%, var(--photo-accent) 78%, var(--photo-deep) 100%);
  }
  .title-bar {
    position: absolute; left: 38px;
    background: var(--brand-blue);
    color: #fff;
    display: flex; align-items: center;
    padding-left: 22px;
    z-index: 1;
  }
  .title-main { top: 55px; width: 380px; height: 56px; font-size: 27px; letter-spacing: 0.3px; font-weight: 400; }
  .title-main strong { font-weight: 700; margin-right: 7px; }
  .title-sub { top: 116px; width: 275px; height: 46px; font-size: 23px; font-weight: 300; }
  .hero-points {
    position: absolute; left: 38px; top: 210px;
    list-style: none;
    color: var(--hero-text);
    font-size: 19px; font-weight: 300; line-height: 27px;
    z-index: 1;
  }
  .hero-points li { padding-left: 19px; position: relative; }
  .hero-points li::before { content: "•"; position: absolute; left: 0; }
  .hero-points .wrap { width: 340px; }

  /* Topic band */
  .topic-band {
    position: absolute; left: 0; top: 389px;
    width: 840px; height: 106px;
    background: var(--band-dark);
    color: #fff;
  }
  .topic-list {
    position: absolute; top: 24px;
    list-style: none;
    font-size: 18.5px; line-height: 28px; font-weight: 400;
  }
  .topic-list li { padding-left: 19px; position: relative; }
  .topic-list li::before { content: "•"; position: absolute; left: 0; }
  .topic-col-1 { left: 38px; }
  .topic-col-2 { left: 190px; }
  .topic-col-3 { left: 393px; }
  .partner-name {
    position: absolute; left: 658px; top: 30px; width: 142px;
    text-align: center;
    font-size: 17px; line-height: 23px; font-weight: 400;
    letter-spacing: 1.5px; color: #fff; text-transform: uppercase;
  }

  /* Programs */
  .programs { position: absolute; left: 0; top: 495px; width: 840px; height: 575px; }
  .program { position: absolute; width: 363px; }
  .program h2 {
    font-family: "Roboto Condensed", "Arial Narrow", sans-serif;
    font-weight: 400; font-size: 15.5px; line-height: 19px;
    color: var(--heading-blue);
    text-transform: uppercase;
    margin-bottom: 7px;
  }
  .program p {
    font-size: 13.2px; line-height: 16.5px; color: var(--ink);
    text-align: justify;
  }
  .col-left { left: 38px; }
  .col-right { left: 443px; width: 357px; }
  .row-1 { top: 36px; }
  .row-2 { top: 148px; }
  .row-3 { top: 267px; }
  .row-4 { top: 402px; }

  .register {
    position: absolute; left: 443px; top: 398px;
    width: 357px; height: 146px;
    background: var(--brand-blue);
    color: #fff; text-align: center;
    padding-top: 22px;
  }
  .register-lead { font-size: 17px; font-weight: 400; }
  .register-phone { font-size: 26px; font-weight: 600; margin-top: 8px; letter-spacing: 0.2px; }
  .register-hours { font-size: 13.2px; line-height: 16.5px; margin-top: 10px; }
  .register-hours .sep { margin: 0 10px; }
</style>
</head>
<body>
  <article class="flyer">
    <header class="hero">
      <div class="hero-photo" role="img" aria-label="Photo of a young girl at a desk using a computer whose screen shows a live video class with the teacher in a large frame and classmates in small frames"></div>
      <h1 class="title-bar title-main"><strong>READING</strong> SKILLS CLASSES</h1>
      <p class="title-bar title-sub">Online this Summer!</p>
      <ul class="hero-points">
        <li>Small class size</li>
        <li>A skilled and encouraging teacher</li>
        <li>Individualized skills instruction</li>
        <li class="wrap">A program of independent reading in great books</li>
      </ul>
    </header>

    <section class="topic-band">
      <ul class="topic-list topic-col-1"><li>Phonics</li><li>Study Skills</li></ul>
      <ul class="topic-list topic-col-2"><li>Comprehension</li><li>Speed Reading</li></ul>
      <ul class="topic-list topic-col-3"><li>Fluency</li><li>Love of Reading</li></ul>
      <p class="partner-name">Northfield<br>University</p>
    </section>

    <section class="programs">
      <div class="program col-left row-1">
        <h2>Program for Preschoolers:</h2>
        <p>Students in this program build strong reading readiness skills. Your child will learn letter recognition and beginning phonics, and develop the motivation and love of reading that make learning to read easy, enjoyable, and successful.</p>
      </div>
      <div class="program col-right row-1">
        <h2>Program for Entering Kindergartners:</h2>
        <p>Students in this program learn beginning reading skills and develop a love of books. Your child will learn letter recognition, phonics, and sight words, and will learn to sound out short words.</p>
      </div>
      <div class="program col-left row-2">
        <h2>Program for Entering 1st Graders:</h2>
        <p>Students in this program learn to read independently. Your child will learn phonics and sight words, build comprehension, and gain the skills and confidence needed for success in first grade.</p>
      </div>
      <div class="program col-right row-2">
        <h2>Program for Entering 2nd Graders:</h2>
        <p>Students in this program become fluent, independent readers. Your child will make significant gains in phonics and word-attack skills, fluency, and comprehension, and will develop confidence and a love of reading.</p>
      </div>
      <div class="program col-left row-3">
        <h2>Program for Entering 3rd Graders:</h2>
        <p>Students in this program become strong independent readers. Your child will develop the comprehension, fluency, and long-word decoding skills needed to read longer books with ease, and will build confidence and a love of reading.</p>
      </div>
      <div class="program col-right row-3">
        <h2>Program for Entering 4th and 5th Graders:</h2>
        <p>Students in this program make substantial gains in comprehension, long-word decoding skills, fluency, and reading speed. Your child will complete homework more quickly and easily, be more successful in school, and become a strong, enthusiastic reader.</p>
      </div>
      <div class="program col-left row-4">
        <h2>Programs for Entering 6th-8th Graders and<br>Entering 9th and 10th Graders:</h2>
        <p>Students in these programs make substantial gains in comprehension while doubling reading speed. They also learn the best way to read textbooks, take notes, and study for tests. As a result, students complete homework more quickly and easily, get better grades, and enjoy reading more.</p>
      </div>
      <aside class="register">
        <p class="register-lead">For More Information or to Register</p>
        <p class="register-phone">Call 1-800-555-0142</p>
        <p class="register-hours">Mon.-Fri.&nbsp;&nbsp;&nbsp;&nbsp;5am–7pm<br>Sat. 5am–4pm<span class="sep">|</span>Sun. 6am–4pm</p>
      </aside>
    </section>
  </article>
</body>
</html>
```